Marlow Creek Nectar Company, local Honey producer needs product Lable to encourage sales

We are a small business (Marlow Creek Nectar Company) located in a small Texas town that harvests honey from our beehives yearly. Our honey would be considered "raw wildflower honey" and our goal is to sell it locally (farmers markets) and to surrounding areas.

We are currently packaging in plastic classic honey bottles with white flip caps. Sizes are 8oz and 16oz bottles (see pictures for actual size). Larger orders will be filled in one quart mason jars.

Design Ideas:
-vintage style design with bee or several bees in background
- incorporate company name "Marlow Creek Nectar Company"
- needs small description "Raw Honey", and "Harvested in Pinebrook Valley"

Target Market(s)

Farmers markets, health conscience people looking for unprocessed food options

Industry/Entity Type

Small Business

Requirements
Nice to have
• Vintage feel
Should not have
• No cartoonish characters

```html
<!DOCTYPE html>
<html lang="en">
<head>
<meta charset="utf-8">
<title>Marlow Creek Nectar Company – Raw Honey Label</title>
<link rel="stylesheet" href="https://fonts.googleapis.com/css2?family=Oswald:wght@500&family=Quicksand:wght@400&family=Lora:ital,wght@1,700&display=swap">
<style>
  :root {
    --ink: #0d0d0d;
    --paper: #ffffff;
    --cream: #ead6aa;
    --honey-orange: #f6a31b;
    --ribbon-tan: #c4974a;
    --bee-gold: #f2b227;
    --bee-brown: #a9803f;
  }
  html, body {
    margin: 0;
    padding: 0;
    overflow: hidden;
  }
  body {
    width: 1200px;
    height: 1000px;
    background: var(--paper);
  }
  .canvas {
    position: relative;
    width: 1200px;
    height: 1000px;
    overflow: hidden;
  }
  .label {
    position: absolute;
    left: 305px;
    top: 47px;
    width: 590px;
    height: 905px;
  }
  .label__border { fill: var(--ink); }
  .label__gap { fill: var(--paper); }
  .label__field { fill: var(--cream); }
  .shield__body { fill: var(--ink); }
  .shield__rule { fill: none; stroke: var(--paper); stroke-width: 2; }
  .ribbon__tail { fill: var(--ribbon-tan); }
  .ribbon__band { fill: var(--honey-orange); }
  .brand-name {
    font-family: "Oswald", sans-serif;
    font-weight: 500;
    font-size: 40px;
    fill: var(--paper);
    letter-spacing: 1px;
  }
  .brand-sub {
    font-family: "Quicksand", sans-serif;
    font-weight: 400;
    font-size: 22px;
    fill: var(--paper);
  }
  .product-type {
    font-family: "Lora", serif;
    font-style: italic;
    font-weight: 700;
    font-size: 13px;
    fill: var(--ink);
    letter-spacing: 0.5px;
  }
  .origin {
    font-family: "Quicksand", sans-serif;
    font-weight: 400;
    font-size: 15.5px;
    fill: var(--ink);
  }
</style>
</head>
<body>
<main class="canvas">
  <svg class="label" viewBox="0 0 460 705" xmlns="http://www.w3.org/2000/svg" aria-label="Marlow Creek Nectar Company raw honey label">
    <defs>
      <linearGradient id="bee-tones" x1="0" y1="0" x2="0" y2="1">
        <stop offset="0" stop-color="#f4f0e6"/>
        <stop offset="0.5" stop-color="#f2b227"/>
        <stop offset="1" stop-color="#a9803f"/>
      </linearGradient>
    </defs>

    <rect class="label__border" x="0" y="0" width="460" height="705" rx="230" ry="260"/>
    <rect class="label__gap" x="14" y="14" width="432" height="677" rx="216" ry="246"/>
    <rect class="label__field" x="22" y="22" width="416" height="661" rx="208" ry="238"/>

    <g class="shield">
      <path class="shield__body" d="M101,100 L229,80 L358,100 L358,394 L229,470 L101,394 Z"/>
      <path class="shield__rule" d="M108,106 L229,87 L351,106 L351,390 L229,462 L108,390 Z"/>
    </g>

    <ellipse class="bee-mark" cx="229" cy="180" rx="48" ry="62" fill="url(#bee-tones)" role="img" aria-label="Illustration of a bee"/>

    <g class="ribbon">
      <path class="ribbon__tail" d="M46,262 L112,262 L112,322 L46,322 L66,292 Z"/>
      <path class="ribbon__tail" d="M412,262 L346,262 L346,322 L412,322 L392,292 Z"/>
      <rect class="ribbon__band" x="80" y="256" width="298" height="72" rx="14"/>
      <text class="brand-name" x="229" y="307" text-anchor="middle">MARLOW CREEK</text>
    </g>

    <text class="brand-sub" x="229" y="370" text-anchor="middle">NECTAR COMPANY</text>

    <text class="product-type" x="229" y="505" text-anchor="middle">★ RAW HONEY ★</text>

    <rect class="hive-mark" x="190" y="535" width="96" height="70" rx="4" fill="#2a2418" role="img" aria-label="Beehive icon with a small flying bee"/>

    <text class="origin" x="229" y="630" text-anchor="middle">Harvested in Pinebrook Valley</text>
  </svg>
</main>
</body>
</html>
```